Modern, Clean, Edgy & Fun Comedy Show Flyer

We need to a create a new flyer for the comedy show, Harbor Laugh Night. The original version of the flyer is attached (file: Old flyer), as well as two versions of the logo.
- The text should be the same except now the show is Every First Wednesday and the next show is June 1.
- Remove the jerk shop logo
- Remove the picture of the man, and replace it with a photo of Delphine (our host), the Audience, or something of your own design.
* pictures of Delphine and the Audience is attached.
* We'd like to keep the same color palette and have also attached a color palette for reference

I have also attached 4 references of flyers that I like, that you can use to get an idea of the theme and aesthetic we are looking for.
* Files: Reference 1, Reference 2, Reference 3, Reference 4
Updates

Colors
3277b5
85acd3
0455a3
eaf1f7
cee9f5
ecf7fb
d5d5d5
e6e6e6

Requirements
Must have
• The harbor laugh night logo attached
• The text as specified in the project description
• An option with Delphine and without

```html
<!DOCTYPE html>
<html lang="en">
<head>
<meta charset="utf-8">
<title>Harbor Laugh Night – Comedy Show Flyer</title>
<link href="https://fonts.googleapis.com/css2?family=Kaushan+Script&family=Audiowide&family=Libre+Baskerville:wght@700&family=Ubuntu:wght@300&display=swap" rel="stylesheet">
<style>
  :root {
    --page-bg: #d5d5d5;
    --sky-top: #5fb0c0;
    --sky-mid: #7fbcc8;
    --navy-band: #2c4472;
    --venue-dark: #2a2430;
    --venue-mid: #4a5560;
    --venue-warm: #5a3f48;
    --host-tone: #3d2a24;
    --host-shadow: #1d1615;
    --white: #ffffff;
    --accent-yellow: #f5e82a;
  }
  * { margin: 0; padding: 0; box-sizing: border-box; }
  html, body { width: 1200px; height: 1200px; overflow: hidden; }
  body { background: var(--page-bg); position: relative; }

  .flyer {
    position: absolute; left: 0; top: 175px;
    width: 1200px; height: 850px; overflow: hidden;
    background: var(--venue-dark);
  }
  .venue-photo {
    position: absolute; inset: 0;
    background:
      linear-gradient(180deg, var(--sky-top) 0%, var(--sky-mid) 20%, rgba(127,188,200,0.55) 34%, rgba(74,85,96,0.2) 55%, transparent 70%),
      radial-gradient(ellipse at 60% 45%, #8a9aa0 0%, transparent 45%),
      linear-gradient(180deg, var(--venue-mid) 30%, var(--venue-warm) 70%, var(--venue-dark) 100%);
  }
  .title-band {
    position: absolute; left: 0; top: 163px; width: 100%; height: 36px;
    background: var(--navy-band);
  }
  .host-photo {
    position: absolute; left: 35px; top: 38px; width: 315px; height: 812px;
    border-radius: 150px 150px 20px 20px;
    background: linear-gradient(180deg, var(--host-tone) 0%, #2a1f1c 45%, var(--host-shadow) 100%);
  }
  .show-title {
    position: absolute; left: 362px; top: 20px;
    font-family: "Kaushan Script", cursive; font-weight: 400; font-size: 108px; line-height: 1;
    color: var(--white); text-shadow: 2px 3px 4px rgba(0,0,0,0.35);
    white-space: nowrap;
  }
  .show-schedule {
    position: absolute; left: 366px; top: 164px;
    font-family: "Libre Baskerville", serif; font-weight: 700; font-size: 26px;
    color: var(--white); line-height: 34px; white-space: nowrap;
  }
  .show-schedule sup { font-size: 14px; }
  .lineup {
    position: absolute; left: 385px; top: 352px;
    font-family: "Audiowide", sans-serif; text-transform: uppercase; white-space: nowrap;
  }
  .lineup-label { color: var(--accent-yellow); font-size: 36px; line-height: 46px; }
  .lineup-name { color: var(--white); font-size: 36px; line-height: 50px; letter-spacing: 1px; }
  .show-name {
    position: absolute; left: 760px; top: 530px; width: 400px;
    font-family: "Audiowide", sans-serif; font-size: 44px; line-height: 54px;
    color: var(--white); text-transform: uppercase; text-align: right;
  }
  .host-details {
    position: absolute; left: 31px; top: 705px;
    font-family: "Audiowide", sans-serif; font-size: 29px; line-height: 40px;
    color: var(--white); text-transform: uppercase; letter-spacing: 2px; white-space: nowrap;
  }
  .venue-details {
    position: absolute; right: 35px; top: 748px;
    font-family: "Ubuntu", sans-serif; font-weight: 300; font-size: 19px; line-height: 24px;
    font-style: normal; color: var(--white); text-align: right; white-space: nowrap;
  }
</style>
</head>
<body>
  <main class="flyer">
    <div class="venue-photo" role="img" aria-label="Photo of a packed comedy club audience under string lights"></div>
    <div class="title-band"></div>
    <div class="host-photo" role="img" aria-label="Photo of host Delphine on stage holding a microphone"></div>

    <h1 class="show-title">Comedy show</h1>
    <p class="show-schedule">every 1<sup>st</sup> Wednesday</p>

    <section class="lineup">
      <p class="lineup-label">Featuring</p>
      <p class="lineup-name">Elliot Brannigan</p>
      <p class="lineup-name">Owen Feldenbaumer</p>
      <p class="lineup-name">Ravi Deshane</p>
      <p class="lineup-name">Tara Okonjo</p>
    </section>

    <p class="show-name">Harbor Laugh Night</p>

    <section class="host-details">
      <p>Hosted by</p>
      <p>Delphine Marrow</p>
      <p>Wednesday, June 1</p>
    </section>

    <address class="venue-details">
      <p>The Lantern Room</p>
      <p>42 Quay Lane, Harborside</p>
      <p>Adm: FREE | Doors 6:30 PM</p>
    </address>
  </main>
</body>
</html>
```